TJ&R Roofing Billboard Design

Looking for a fresh new billboard design with my new headshot photo and using some info from my previous billboard and maybe website for design/content inspiration. My website is https://tjrroofing-example.com/

Also attached are my logo and current lawn sign design. I am looking for something simple, clean and modern. The landing page website should be 3182roof-example.com like my previous billboard has.

```html
<!DOCTYPE html>
<html lang="en">
<head>
<meta charset="UTF-8">
<title>TJ&amp;R Roofing Billboard</title>
<link href="https://fonts.googleapis.com/css2?family=Montserrat:wght@600;700;800&family=Merriweather:wght@700&display=swap" rel="stylesheet">
<style>
  :root {
    --navy: #14284b;
    --band: #0b2247;
    --green: #3aa648;
    --lime: #a8d43c;
    --white: #ffffff;
    --ink: #111111;
    --page: #e4e9ef;
    --sky-light: #f3f8fd;
    --sky-blue: #a9d2f3;
    --roof-light: #b9ab98;
    --roof-dark: #8a7c6b;
    --shirt: #c9d6ea;
  }
  * { box-sizing: border-box; margin: 0; padding: 0; }
  html, body { width: 1200px; height: 801px; overflow: hidden; }
  body {
    background: var(--page);
    font-family: "Montserrat", sans-serif;
    position: relative;
  }
  .billboard {
    position: absolute;
    left: 20px;
    top: 245px;
    width: 1160px;
    height: 312px;
    overflow: hidden;
    background: linear-gradient(100deg, var(--sky-light) 0%, #e3f0fb 45%, var(--sky-blue) 100%);
  }
  .roof-photo {
    position: absolute;
    left: 690px;
    top: 70px;
    width: 470px;
    height: 185px;
    background: linear-gradient(160deg, var(--roof-light) 0%, var(--roof-dark) 100%);
    clip-path: polygon(18% 0, 100% 0, 100% 100%, 0 100%, 0 45%);
  }
  .headshot {
    position: absolute;
    left: 830px;
    top: 30px;
    width: 310px;
    height: 282px;
    background: linear-gradient(180deg, #9c8a7a 0%, #b7c5dc 45%, var(--shirt) 100%);
    border-radius: 130px 130px 0 0;
    z-index: 2;
  }
  .brand {
    position: absolute;
    left: 45px;
    top: 20px;
    display: flex;
    align-items: center;
    gap: 20px;
  }
  .brand-mark {
    width: 88px;
    height: 88px;
    border-radius: 50%;
    background: var(--green);
    flex: none;
  }
  .brand-name {
    font-weight: 700;
    font-size: 46px;
    color: var(--navy);
    line-height: 1;
  }
  .brand-tagline {
    font-family: "Merriweather", serif;
    font-weight: 700;
    font-size: 21px;
    color: var(--navy);
    margin-top: 6px;
  }
  .headline {
    position: absolute;
    left: 38px;
    top: 132px;
    font-weight: 800;
    line-height: 0.98;
  }
  .headline-top { color: var(--navy); font-size: 44px; display: block; }
  .headline-bottom { color: var(--green); font-size: 53px; display: block; letter-spacing: -0.5px; }
  .price-lead {
    position: absolute;
    left: 580px;
    top: 138px;
    font-size: 26px;
    font-weight: 600;
    color: var(--ink);
  }
  .price-tag {
    position: absolute;
    left: 640px;
    top: 172px;
    width: 160px;
    height: 68px;
    background: var(--lime);
    border-radius: 6px;
    transform: rotate(-6deg);
    display: flex;
    align-items: center;
    justify-content: center;
    font-size: 38px;
    font-weight: 800;
    color: var(--ink);
  }
  .contact-band {
    position: absolute;
    left: 0;
    top: 253px;
    width: 1160px;
    height: 59px;
    background: var(--band);
    display: flex;
    align-items: center;
    padding-left: 28px;
    gap: 14px;
  }
  .contact-icon {
    width: 40px;
    height: 40px;
    border-radius: 50%;
    background: var(--green);
    display: flex;
    align-items: center;
    justify-content: center;
    flex: none;
  }
  .contact-phone {
    font-size: 48px;
    font-weight: 800;
    color: var(--white);
    margin-right: 10px;
    line-height: 1;
  }
  .contact-web {
    font-size: 25px;
    font-weight: 800;
    color: var(--white);
  }
</style>
</head>
<body>
  <section class="billboard">
    <div class="roof-photo" role="img" aria-label="Photo of a house roof with asphalt shingles"></div>

    <div class="brand">
      <div class="brand-mark"></div>
      <div>
        <div class="brand-name">TJ&amp;R Roofing LLC</div>
        <div class="brand-tagline">Built Strong, Built to Last</div>
      </div>
    </div>

    <h1 class="headline">
      <span class="headline-top">EXPERT ROOF</span>
      <span class="headline-bottom">REPLACEMENTS</span>
    </h1>

    <div class="price-lead">Starting at</div>
    <div class="price-tag">$7,499</div>

    <div class="contact-band">
      <span class="contact-icon">
        <svg width="22" height="22" viewBox="0 0 24 24" aria-hidden="true">
          <path fill="#fff" d="M6.6 10.8a15.1 15.1 0 0 0 6.6 6.6l2.2-2.2a1 1 0 0 1 1-.25 11.4 11.4 0 0 0 3.6.57 1 1 0 0 1 1 1V20a1 1 0 0 1-1 1A17 17 0 0 1 3 4a1 1 0 0 1 1-1h3.5a1 1 0 0 1 1 1c0 1.250.2 2.45.57 3.57a1 1 0 0 1-.25 1z"/>
        </svg>
      </span>
      <span class="contact-phone">555·201·7734</span>
      <span class="contact-icon">
        <svg width="22" height="22" viewBox="0 0 24 24" aria-hidden="true">
          <rect x="5" y="5" width="14" height="10" rx="1" fill="none" stroke="#fff" stroke-width="2"/>
          <rect x="2" y="16" width="20" height="3" rx="1" fill="#fff"/>
        </svg>
      </span>
      <span class="contact-web">3182ROOF-EXAMPLE.COM</span>
    </div>

    <div class="headshot" role="img" aria-label="Headshot of the company owner in a light blue shirt"></div>
  </section>
</body>
</html>
```